Business Cards and Stationary for a new consulting, recruiting and outsourcing company in Germany
BRAUNFELD Consulting
Business Cards and Stationary for a new consulting, recruiting and outsourcing company in Germany  - Consulting
Creative Brief
Professional
BRAUNFELD Consulting (Company Name) Ramune Braunfeld (First name, last name)
Inhaberin ("Owner" for english version)
Im Lindgrund 5 89512 Tannbach Deutschland ("Germany" for english version)
ramune.braunfeld@braunfeld-beratung.example
htttps://www.braunfeld-beratung.example
The round logo version with black background size around 75% of the card.

```html
<!DOCTYPE html>
<html lang="en">
<head>
<meta charset="utf-8">
<title>BRAUNFELD Consulting – Stationery</title>
<link rel="stylesheet" href="https://fonts.googleapis.com/css2?family=Open+Sans:wght@400;600;700&display=swap">
<style>
  :root {
    --bg: #eceef0;
    --paper: #ffffff;
    --ink: #3a3a3a;
    --muted: #7a7a7a;
    --blue: #29a8e6;
    --orange: #f7941d;
    --card-dark: #111111;
    --brand-dot: #2a9fd8;
  }
  * { box-sizing: border-box; margin: 0; padding: 0; }
  html, body { width: 1200px; height: 936px; overflow: hidden; }
  body {
    background: var(--bg);
    font-family: "Open Sans", Arial, sans-serif;
    color: var(--ink);
    position: relative;
  }
  .sheet {
    position: absolute;
    background: var(--paper);
    box-shadow: 0 2px 8px rgba(0,0,0,.12);
    overflow: hidden;
  }
  .footer-band { position: absolute; left: 0; bottom: 0; width: 100%; display: block; }

  .brand { display: flex; align-items: center; gap: 8px; }
  .brand-dot { border-radius: 50%; background: var(--brand-dot); flex: none; }
  .brand-name { font-weight: 600; color: var(--ink); line-height: 1; white-space: nowrap; }

  /* Letterhead */
  .letterhead { left: 147px; top: 63px; width: 423px; height: 570px; }
  .letterhead .brand { position: absolute; left: 34px; top: 32px; }
  .letterhead .brand-dot { width: 20px; height: 20px; }
  .letterhead .brand-name { font-size: 13px; }
  .letterhead-contact {
    position: absolute; right: 28px; top: 30px; text-align: right;
    font-size: 5px; line-height: 1.6; color: var(--muted);
  }
  .letter-body {
    position: absolute; left: 34px; top: 96px; width: 355px;
    font-size: 6px; line-height: 1.55; color: var(--muted);
  }
  .letter-body p { margin-bottom: 9px; }
  .letter-signature { font-size: 9px; color: var(--ink); margin: 6px 0 4px; }

  /* Folder */
  .folder { left: 632px; top: 63px; width: 456px; height: 570px; }
  .folder .brand { position: absolute; left: 0; right: 0; top: 250px; justify-content: center; gap: 10px; }
  .folder .brand-dot { width: 34px; height: 34px; }
  .folder .brand-name { font-size: 22px; }
  .folder-web {
    position: absolute; right: 28px; bottom: 22px; font-size: 9px;
    color: #fff; letter-spacing: .12em;
  }

  /* Business cards */
  .card-front { left: 46px; top: 678px; width: 207px; height: 82px; }
  .card-front .brand { position: absolute; left: 10px; top: 10px; gap: 5px; }
  .card-front .brand-dot { width: 10px; height: 10px; }
  .card-front .brand-name { font-size: 7.5px; }
  .card-person { position: absolute; left: 10px; top: 30px; font-size: 4.5px; line-height: 1.45; color: var(--muted); }
  .card-person strong { color: var(--ink); font-size: 5.5px; }
  .card-contact { position: absolute; left: 92px; top: 30px; width: 110px; font-size: 4px; line-height: 1.55; color: var(--muted); }

  .card-back { left: 46px; top: 772px; width: 207px; height: 88px; background: var(--card-dark); }
  .card-back .brand { position: absolute; left: 0; right: 0; top: 35px; justify-content: center; gap: 6px; }
  .card-back .brand-dot { width: 18px; height: 18px; }
  .card-back .brand-name { color: #fff; font-size: 11px; }

  /* Envelope front */
  .envelope { left: 266px; top: 678px; width: 448px; height: 195px; }
  .envelope .brand { position: absolute; left: 24px; top: 22px; gap: 7px; }
  .envelope .brand-dot { width: 18px; height: 18px; }
  .envelope .brand-name { font-size: 12px; }
  .envelope-web {
    position: absolute; left: 30px; bottom: 40px; font-size: 7px;
    color: var(--blue); letter-spacing: .12em;
  }

  /* Envelope back */
  .envelope-back { left: 740px; top: 678px; width: 354px; height: 195px; }
  .envelope-flap {
    position: absolute; left: 0; top: 0; width: 100%; height: 62px;
    background: var(--blue); border-bottom-left-radius: 40px; border-bottom-right-radius: 40px;
  }
  .envelope-flap span {
    position: absolute; right: 22px; top: 24px; font-size: 9px; color: #fff; letter-spacing: .12em;
  }
</style>
</head>
<body>

  <section class="sheet letterhead">
    <div class="brand">
      <span class="brand-dot"></span>
      <span class="brand-name">BRAUNFELD Consulting</span>
    </div>
    <div class="letterhead-contact">
      Im Lindgrund 5<br>89512 Tannbach<br>Deutschland<br>ramune.braunfeld@braunfeld-beratung.example<br>htttps://www.braunfeld-beratung.example
    </div>
    <div class="letter-body">
      <p>12 May 2024</p>
      <p>Dear Client,</p>
      <p>Thank you for your interest in our consulting services. We support growing companies with recruiting, outsourcing and strategic advice tailored to the German market and its specific needs.</p>
      <p>Our team combines long experience with a personal approach, so every project receives clear planning and reliable results.</p>
      <p>We look forward to working with you and will gladly arrange a first meeting at your convenience.</p>
      <p>Kind regards,</p>
      <div class="letter-signature">R. Braunfeld</div>
      <p>Ramune Braunfeld<br>Inhaberin</p>
    </div>
    <svg class="footer-band" viewBox="0 0 423 60" height="60" preserveAspectRatio="none" aria-hidden="true">
      <path d="M0 28 Q211 8 423 28 L423 60 L0 60 Z" fill="var(--blue)"/>
      <path d="M0 22 Q211 2 423 22" fill="none" stroke="var(--orange)" stroke-width="2"/>
    </svg>
  </section>

  <section class="sheet folder">
    <div class="brand">
      <span class="brand-dot"></span>
      <span class="brand-name">BRAUNFELD Consulting</span>
    </div>
    <svg class="footer-band" viewBox="0 0 456 80" height="80" preserveAspectRatio="none" aria-hidden="true">
      <path d="M0 30 Q228 6 456 30 L456 80 L0 80 Z" fill="var(--blue)"/>
      <path d="M0 22 Q228 -2 456 22" fill="none" stroke="var(--orange)" stroke-width="2.5"/>
    </svg>
    <span class="folder-web">www.braunfeld-beratung.example</span>
  </section>

  <section class="sheet card-front">
    <div class="brand">
      <span class="brand-dot"></span>
      <span class="brand-name">BRAUNFELD Consulting</span>
    </div>
    <div class="card-person"><strong>Ramune Braunfeld</strong><br>Inhaberin</div>
    <div class="card-contact">Im Lindgrund 5, 89512 Tannbach<br>ramune.braunfeld@braunfeld-beratung.example<br>htttps://www.braunfeld-beratung.example</div>
    <svg class="footer-band" viewBox="0 0 207 14" height="14" preserveAspectRatio="none" aria-hidden="true">
      <path d="M0 7 Q103 2 207 7 L207 14 L0 14 Z" fill="var(--blue)"/>
      <path d="M0 5 Q103 0 207 5" fill="none" stroke="var(--orange)" stroke-width="1"/>
    </svg>
  </section>

  <section class="sheet card-back">
    <div class="brand">
      <span class="brand-dot"></span>
      <span class="brand-name">BRAUNFELD Consulting</span>
    </div>
  </section>

  <section class="sheet envelope">
    <div class="brand">
      <span class="brand-dot"></span>
      <span class="brand-name">BRAUNFELD Consulting</span>
    </div>
    <span class="envelope-web">www.braunfeld-beratung.example</span>
    <svg class="footer-band" viewBox="0 0 448 28" height="28" preserveAspectRatio="none" aria-hidden="true">
      <path d="M0 12 Q224 2 448 12 L448 28 L0 28 Z" fill="var(--blue)"/>
      <path d="M0 8 Q224 -2 448 8" fill="none" stroke="var(--orange)" stroke-width="1.5"/>
    </svg>
  </section>

  <section class="sheet envelope-back">
    <div class="envelope-flap"><span>www.braunfeld-beratung.example</span></div>
  </section>

</body>
</html>
```